New florist business website design

Number 1 want is an easy to navigate & check out website
Needs to be beautiful and eye catching as well.
This is an online only business (no shop front)
Rustic and blush pinks, neutrals, woods, leaves
Customers need to be able to go onto my website, select something they want to buy but have the option to use a drop down box to change colours of the flowers, or add notes to make changes to the arrangement

Industry/Entity Type

Florist

Coding

Coded - Design and coding required

Number of Pages Required

5+ page

Colors
f9d9e8
fff2ec
fffefc

Requirements
Must have
• Drop down menu to take you to other pages for Arrangements, bouquets, everlasting arrangements, gifts, contact
Be able to purchase and “add to basket”
Checkout page
Nice to have
• Be able to add my own photos once I’ve taken new ones
Should not have
• Tacky images or clip art

```html
<!DOCTYPE html>
<html lang="en">
<head>
<meta charset="utf-8">
<title>Petal &amp; Twine — Florist</title>
<link href="https://fonts.googleapis.com/css2?family=Kanit:wght@300;400;500&family=Pacifico&display=swap" rel="stylesheet">
<style>
:root{
  --cream:#fbf1ee;
  --blush:#fde4e4;
  --rose:#e6adb3;
  --rose-deep:#d9959c;
  --teal:#0c6e6e;
  --ink:#3a3434;
  --line:#ead3d3;
  --white:#fffefc;
}
*{margin:0;padding:0;box-sizing:border-box}
html,body{width:1200px;height:2558px;overflow:hidden;background:var(--cream)}
body{font-family:"Kanit",sans-serif;color:var(--ink)}
.page{position:relative;width:1208px;height:2576px;transform:scale(.9934);transform-origin:0 0;background:var(--cream)}
.abs{position:absolute}
.script{font-family:"Pacifico",cursive;font-weight:400;color:var(--ink)}
.btn{position:absolute;background:var(--teal);color:#fff;font-size:11px;font-weight:400;display:flex;align-items:center;justify-content:center;border-radius:4px;letter-spacing:.2px}

/* header */
.brand{left:150px;top:44px;font-size:22px;font-weight:300;color:var(--ink);display:flex;align-items:center;gap:8px}
.brand-dot{width:14px;height:14px;border-radius:50%;border:1px solid var(--ink)}
.nav{left:420px;top:58px;display:flex;align-items:center;gap:29px;font-size:9.5px;color:var(--teal);text-transform:uppercase;letter-spacing:.1px}
.nav .login{border:1.5px solid var(--teal);border-radius:10px;padding:1px 9px;margin-left:-10px}
.cart-top{left:1032px;top:55px}

/* hero */
.hero-title{left:200px;top:180px;width:420px;text-align:center;font-size:44px;line-height:46px}
.hero-sub{left:200px;top:284px;width:420px;text-align:center;font-size:15px;font-weight:300}
.hero-art{left:670px;top:120px;width:385px;height:300px;border-radius:50%;background:radial-gradient(circle at 55% 50%,#f4f1ef 0 22%,#c9555d 30%,#e0a4a8 45%,#5f8a5a 62%,transparent 72%)}
.hero-ring{left:740px;top:160px;width:290px;height:250px;border-radius:50%;border:1.5px solid var(--rose)}
.wave{left:0;top:320px}

/* features */
.blush-band{left:0;top:430px;width:1208px;height:340px;background:var(--blush)}
.feature{position:absolute;top:537px;width:220px;text-align:center}
.feature .badge{width:120px;height:120px;border-radius:50%;background:var(--cream);margin:0 auto;display:flex;align-items:center;justify-content:center}
.feature p{margin-top:30px;font-size:15.5px;font-weight:300}

/* catalog panel */
.panel{left:10px;top:768px;width:1198px;height:1172px;background:var(--cream)}
.section-title{width:1208px;left:0;text-align:center;font-size:24px}
.step-line{left:264px;top:934px;width:680px;height:1px;background:#cfc6c6}
.step{position:absolute;top:898px;width:74px;height:74px;border-radius:50%;border:2px solid var(--rose);background:var(--cream);color:var(--teal);font-size:26px;font-weight:300;display:flex;align-items:center;justify-content:center}
.step.active{border-color:var(--teal)}
.step-label{position:absolute;top:992px;width:200px;text-align:center;font-size:11px;font-weight:300}

.tabs{left:152px;top:1135px;width:905px;height:45px;background:var(--rose);border-radius:3px;display:flex;align-items:center;font-size:11px;color:var(--ink)}
.tab-active{background:var(--teal);color:#fff;width:116px;height:45px;display:flex;align-items:center;justify-content:center;border-radius:3px 0 0 3px}
.tab{margin-left:30px}
.tab + .tab{margin-left:31px}
.color-label{position:absolute;right:92px;top:26px;font-size:11px;font-weight:500}
.select{position:absolute;right:4px;top:4px;width:82px;height:36px;background:var(--white);border:2px solid var(--teal);border-radius:4px;font-size:11px;display:flex;align-items:center;justify-content:space-between;padding:0 10px 0 12px}

.grid{left:152px;top:1219px;width:905px;height:595px;display:grid;grid-template-columns:repeat(4,1fr);grid-template-rows:repeat(2,1fr);border:1px solid var(--line)}
.card{border:1px solid var(--line);position:relative;padding:14px 14px 0}
.card .photo{width:196px;height:196px}
.card .meta{display:flex;justify-content:space-between;margin-top:14px;font-size:11px;font-weight:300}
.card .name{color:var(--teal)}
.card .actions{display:flex;align-items:center;gap:8px;margin-top:16px;font-size:11px;color:var(--teal)}
.card .details{margin-left:auto;text-decoration:underline}
.cart-chip{width:30px;height:30px;border-radius:50%;background:var(--rose);display:flex;align-items:center;justify-content:center}
.card.lifted{position:absolute;left:367px;top:1203px;width:249px;height:327px;background:var(--white);box-shadow:0 2px 10px rgba(0,0,0,.12);border:none;padding:16px 16px 0}
.card.lifted .photo{width:216px;height:216px}

.pages{left:518px;top:1834px;display:flex;gap:18px}
.pages span{width:46px;height:46px;border-radius:50%;border:2px solid var(--rose);display:flex;align-items:center;justify-content:center;font-size:20px;font-weight:300}
.pages span.current{border-color:var(--teal)}

/* request */
.lower{left:0;top:1940px;width:1208px;height:522px;background:var(--blush)}
.request-photo{left:151px;top:2003px;width:395px;height:259px;border-radius:6px;background:linear-gradient(120deg,#6e5a4e 0%,#e8e2dc 35%,#f0d6d6 55%,#c9475a 75%,#7a5c48 100%)}
.request-title{left:624px;top:1990px;font-size:40px;line-height:46px;width:420px}
.request-text{left:629px;top:2106px;width:360px;font-size:13px;font-weight:300;line-height:16px;letter-spacing:.3px}

.subscribe{left:279px;top:2300px;width:650px;height:102px;background:var(--cream);border-radius:4px}
.subscribe h3{position:absolute;left:17px;top:16px;font-size:21px}
.field{position:absolute;top:55px;width:245px;height:32px;border:1.5px solid var(--rose);border-radius:6px;font-size:11px;font-weight:300;padding-left:15px;display:flex;align-items:center;color:#5a5252}

/* footer */
.footer{left:0;top:2462px;width:1208px;height:114px;background:var(--rose)}
.footer .brand{left:160px;top:40px;font-size:17px}
.foot-nav{left:353px;top:48px;display:flex;gap:18px;font-size:10px;text-transform:uppercase}
.phone{left:955px;top:34px;font-size:9px}
.social{left:955px;top:54px;display:flex;gap:14px}
.social span{width:19px;height:19px;border-radius:50%;background:var(--ink)}
.copy{left:0;width:1208px;top:102px;text-align:center;font-size:9px}
</style>
</head>
<body>
<div class="page">

  <!-- header -->
  <div class="abs brand"><span class="brand-dot"></span>Petal &amp; Twine</div>
  <nav class="abs nav">
    <span>Arrangements</span><span>Bouquets</span><span>Everlasting Arrangements</span><span>Gifts</span><span>Contact</span><span>Sign up</span><span class="login">Login</span>
  </nav>
  <svg class="abs cart-top" width="26" height="26" viewBox="0 0 26 26" fill="none" stroke="#0c6e6e" stroke-width="2"><path d="M2 4h4l3 12h12l3-9H8"/><circle cx="10" cy="21" r="1.8"/><circle cx="19" cy="21" r="1.8"/></svg>

  <!-- hero -->
  <h1 class="abs script hero-title">Flowers are more than words</h1>
  <p class="abs hero-sub">We know the language of flowers.</p>
  <div class="btn" style="left:329px;top:318px;width:140px;height:29px">CHECK BOUQUET</div>

  <div class="blush-band abs"></div>
  <svg class="abs wave" width="1208" height="160" viewBox="0 0 1208 160">
    <path d="M0 0 Q600 230 1208 70 V160 H0Z" fill="#fde4e4"/>
    <path d="M0 22 Q600 260 1208 90" fill="none" stroke="#e6adb3" stroke-width="14"/>
    <path d="M0 0 Q600 230 1208 70" fill="none" stroke="#f6c9cc" stroke-width="4"/>
  </svg>
  <div class="abs hero-ring"></div>
  <div class="abs hero-art" role="img" aria-label="Illustrated bouquet of white and red roses with green leaves over a blush circle"></div>

  <!-- features -->
  <div class="feature" style="left:140px">
    <div class="badge"><svg width="74" height="60" viewBox="0 0 74 60" fill="none" stroke="#3a3434" stroke-width="2.2"><rect x="4" y="14" width="44" height="32" rx="2"/><path d="M48 24h12l8 10v12H48"/><circle cx="18" cy="48" r="5"/><circle cx="58" cy="48" r="5"/><path d="M20 14 26 4l6 10"/></svg></div>
    <p>Free delivery all orders</p>
  </div>
  <div class="feature" style="left:376px">
    <div class="badge"><svg width="60" height="70" viewBox="0 0 60 70" fill="none" stroke="#3a3434" stroke-width="2.2"><circle cx="30" cy="16" r="8"/><circle cx="18" cy="26" r="8"/><circle cx="42" cy="26" r="8"/><path d="M14 34 30 44 46 34 30 50Z"/><path d="M30 50 12 66"/></svg></div>
    <p>Fresh&nbsp; flower delivery</p>
  </div>
  <div class="feature" style="left:612px">
    <div class="badge"><svg width="80" height="72" viewBox="0 0 80 72" fill="none" stroke="#3a3434" stroke-width="2.2"><circle cx="32" cy="42" r="26"/><text x="32" y="51" text-anchor="middle" font-family="Kanit,sans-serif" font-size="24" font-weight="300" fill="#3a3434" stroke="none">24</text><rect x="46" y="4" width="28" height="20" rx="2"/><path d="M52 11h16M52 17h12"/></svg></div>
    <p>24 hours 7 days service</p>
  </div>
  <div class="feature" style="left:848px">
    <div class="badge"><svg width="80" height="70" viewBox="0 0 80 70" fill="none" stroke="#3a3434" stroke-width="2.2"><circle cx="44" cy="18" r="14"/><text x="44" y="25" text-anchor="middle" font-family="Kanit,sans-serif" font-size="19" fill="#3a3434" stroke="none">$</text><path d="M4 50h14l14 4h14l20-12-4-4-20 8H32M4 62h50l22-16"/></svg></div>
    <p>Money back guarantee</p>
  </div>

  <!-- catalog panel -->
  <div class="abs panel"></div>
  <h2 class="abs script section-title" style="top:818px">Delivery and payment</h2>
  <div class="abs step-line"></div>
  <div class="step active" style="left:227px">1</div>
  <div class="step" style="left:453px">2</div>
  <div class="step" style="left:680px">3</div>
  <div class="step" style="left:906px">4</div>
  <div class="step-label" style="left:164px">Pick Your Flowers</div>
  <div class="step-label" style="left:390px">Add A Vase / Wrapping</div>
  <div class="step-label" style="left:617px">Add Chocolates / Gift</div>
  <div class="step-label" style="left:843px">Add Delivery Info / Payment</div>

  <h2 class="abs script section-title" style="top:1057px">Catlog</h2>
  <div class="abs tabs">
    <div class="tab-active">POPULER</div>
    <span class="tab">NEW</span><span class="tab">FAVOURITE</span>
    <span class="color-label">Select Color:</span>
    <div class="select">ALL <svg width="14" height="9" viewBox="0 0 14 9" fill="none" stroke="#3a3434" stroke-width="2"><path d="M1 1l6 6 6-6"/></svg></div>
  </div>

  <div class="abs grid">
    <div class="card"><div class="photo" role="img" aria-label="Pastel bouquet of roses and lilac flowers in pink wrap" style="background:linear-gradient(135deg,#f3c9d2,#f7ecea 45%,#b77fb8)"></div>
      <div class="meta"><span class="name">Golden Gory</span><span>$39.00</span></div>
      <div class="actions"><span class="cart-chip"><svg width="16" height="16" viewBox="0 0 26 26" fill="none" stroke="#0c6e6e" stroke-width="2.4"><path d="M2 4h4l3 12h12l3-9H8"/><circle cx="10" cy="21" r="1.8"/><circle cx="19" cy="21" r="1.8"/></svg></span><svg width="24" height="22" viewBox="0 0 24 22" fill="none" stroke="#0c6e6e" stroke-width="1.6"><path d="M12 20S2 13.5 2 7.5A5 5 0 0 1 12 5a5 5 0 0 1 10 2.5C22 13.5 12 20 12 20Z"/></svg><span class="details">View details</span></div></div>
    <div class="card"></div>
    <div class="card"><div class="photo" role="img" aria-label="Bright bouquet of orange and red gerberas" style="background:linear-gradient(135deg,#f06a2a,#f7b23c 50%,#d9362e)"></div>
      <div class="meta"><span class="name">Tropical Touch</span><span>$41.00</span></div>
      <div class="actions"><span class="cart-chip"><svg width="16" height="16" viewBox="0 0 26 26" fill="none" stroke="#0c6e6e" stroke-width="2.4"><path d="M2 4h4l3 12h12l3-9H8"/><circle cx="10" cy="21" r="1.8"/><circle cx="19" cy="21" r="1.8"/></svg></span><svg width="24" height="22" viewBox="0 0 24 22" fill="none" stroke="#0c6e6e" stroke-width="1.6"><path d="M12 20S2 13.5 2 7.5A5 5 0 0 1 12 5a5 5 0 0 1 10 2.5C22 13.5 12 20 12 20Z"/></svg><span class="details">View details</span></div></div>
    <div class="card"><div class="photo" role="img" aria-label="Yellow and white daisy bouquet in kraft paper" style="background:linear-gradient(135deg,#e9e070,#fbf7e2 50%,#a38a66)"></div>
      <div class="meta"><span class="name">White Elegance</span><span>$39.00</span></div>
      <div class="actions"><span class="cart-chip"><svg width="16" height="16" viewBox="0 0 26 26" fill="none" stroke="#0c6e6e" stroke-width="2.4"><path d="M2 4h4l3 12h12l3-9H8"/><circle cx="10" cy="21" r="1.8"/><circle cx="19" cy="21" r="1.8"/></svg></span><svg width="24" height="22" viewBox="0 0 24 22"><path d="M12 20S2 13.5 2 7.5A5 5 0 0 1 12 5a5 5 0 0 1 10 2.5C22 13.5 12 20 12 20Z" fill="#d8393b"/></svg><span class="details">View details</span></div></div>
    <div class="card"><div class="photo" role="img" aria-label="Pink gerbera bouquet in purple wrap" style="background:linear-gradient(135deg,#9c3fa8,#f07ab0 50%,#d7d2da)"></div>
      <div class="meta"><span class="name">Simply the Best</span><span>$12.00</span></div>
      <div class="actions"><span class="cart-chip"><svg width="16" height="16" viewBox="0 0 26 26" fill="none" stroke="#0c6e6e" stroke-width="2.4"><path d="M2 4h4l3 12h12l3-9H8"/><circle cx="10" cy="21" r="1.8"/><circle cx="19" cy="21" r="1.8"/></svg></span><svg width="24" height="22" viewBox="0 0 24 22" fill="none" stroke="#0c6e6e" stroke-width="1.6"><path d="M12 20S2 13.5 2 7.5A5 5 0 0 1 12 5a5 5 0 0 1 10 2.5C22 13.5 12 20 12 20Z"/></svg><span class="details">View details</span></div></div>
    <div class="card"><div class="photo" role="img" aria-label="Pastel pink gerbera bouquet in clear wrap" style="background:linear-gradient(135deg,#6a3ea0,#f39a9a 45%,#eae6e2)"></div>
      <div class="meta"><span class="name">Pastel delight Bouquet</span><span>$17.00</span></div>
      <div class="actions"><span class="cart-chip"><svg width="16" height="16" viewBox="0 0 26 26" fill="none" stroke="#0c6e6e" stroke-width="2.4"><path d="M2 4h4l3 12h12l3-9H8"/><circle cx="10" cy="21" r="1.8"/><circle cx="19" cy="21" r="1.8"/></svg></span><svg width="24" height="22" viewBox="0 0 24 22" fill="none" stroke="#0c6e6e" stroke-width="1.6"><path d="M12 20S2 13.5 2 7.5A5 5 0 0 1 12 5a5 5 0 0 1 10 2.5C22 13.5 12 20 12 20Z"/></svg><span class="details">View details</span></div></div>
    <div class="card"><div class="photo" role="img" aria-label="White chrysanthemum bouquet in black wrap" style="background:linear-gradient(135deg,#eceae4,#2b2b2b 50%,#d5562f)"></div>
      <div class="meta"><span class="name">Pearly White</span><span>$14.00</span></div>
      <div class="actions"><span class="cart-chip"><svg width="16" height="16" viewBox="0 0 26 26" fill="none" stroke="#0c6e6e" stroke-width="2.4"><path d="M2 4h4l3 12h12l3-9H8"/><circle cx="10" cy="21" r="1.8"/><circle cx="19" cy="21" r="1.8"/></svg></span><svg width="24" height="22" viewBox="0 0 24 22" fill="none" stroke="#0c6e6e" stroke-width="1.6"><path d="M12 20S2 13.5 2 7.5A5 5 0 0 1 12 5a5 5 0 0 1 10 2.5C22 13.5 12 20 12 20Z"/></svg><span class="details">View details</span></div></div>
    <div class="card"><div class="photo" role="img" aria-label="Lily and gerbera bouquet with yellow and pink blooms" style="background:linear-gradient(135deg,#e9e25a,#6a8f3c 40%,#f29aa8 70%,#e8553f)"></div>
      <div class="meta"><span class="name">Fragrant pink posy</span><span>$39.00</span></div>
      <div class="actions"><span class="cart-chip"><svg width="16" height="16" viewBox="0 0 26 26" fill="none" stroke="#0c6e6e" stroke-width="2.4"><path d="M2 4h4l3 12h12l3-9H8"/><circle cx="10" cy="21" r="1.8"/><circle cx="19" cy="21" r="1.8"/></svg></span><svg width="24" height="22" viewBox="0 0 24 22" fill="none" stroke="#0c6e6e" stroke-width="1.6"><path d="M12 20S2 13.5 2 7.5A5 5 0 0 1 12 5a5 5 0 0 1 10 2.5C22 13.5 12 20 12 20Z"/></svg><span class="details">View details</span></div></div>
  </div>

  <div class="card lifted"><div class="photo" role="img" aria-label="Bouquet of orchids and hydrangea in kraft paper" style="background:linear-gradient(135deg,#7d8c96,#e9c9a6 40%,#c04c9c 60%,#a9d4dc)"></div>
    <div class="meta"><span class="name">kiss from a rose</span><span>$17.00</span></div>
    <div class="actions"><span class="cart-chip"><svg width="16" height="16" viewBox="0 0 26 26" fill="none" stroke="#0c6e6e" stroke-width="2.4"><path d="M2 4h4l3 12h12l3-9H8"/><circle cx="10" cy="21" r="1.8"/><circle cx="19" cy="21" r="1.8"/></svg></span><svg width="24" height="22" viewBox="0 0 24 22" fill="none" stroke="#0c6e6e" stroke-width="1.6"><path d="M12 20S2 13.5 2 7.5A5 5 0 0 1 12 5a5 5 0 0 1 10 2.5C22 13.5 12 20 12 20Z"/></svg><span class="details">View details</span></div></div>

  <div class="abs pages"><span class="current">1</span><span>2</span><span>3</span></div>

  <!-- request -->
  <div class="abs lower"></div>
  <div class="abs request-photo" role="img" aria-label="Florist wrapping a gift box beside pink roses and red yarn on a table"></div>
  <h2 class="abs script request-title">Didn't find the desided bouquet</h2>
  <p class="abs request-text">leave a request and we will call you back to select a bouquet for any occasion</p>
  <div class="btn" style="left:624px;top:2149px;width:110px;height:29px">PICK BOUQUET</div>

  <div class="abs subscribe">
    <h3 class="script">Subscribe our news later</h3>
    <div class="field" style="left:16px">Enter your name</div>
    <div class="field" style="left:276px">Email address</div>
    <div class="btn" style="left:536px;top:55px;width:98px;height:31px">SUBSCRIBE</div>
  </div>

  <!-- footer -->
  <footer class="abs footer">
    <div class="abs brand"><span class="brand-dot"></span>Petal &amp; Twine</div>
    <div class="abs foot-nav"><span>Arrangements</span><span>|</span><span>Bouquets</span><span>|</span><span>Everlasting Arrangements</span><span>|</span><span>Gifts</span><span>|</span><span>Contact</span></div>
    <div class="abs phone">+(123) 555-010-246</div>
    <div class="abs social"><span></span><span></span><span></span></div>
    <div class="abs copy">© Petal &amp; Twine 2021</div>
  </footer>
</div>
</body>
</html>
```